Business Card for Lawyer

I'm looking for a business card for my new law firm, based in Ontario, Canada. I would prefer single sided. I am partial (but not limited) to white and blue color wise and like things understated. Also, if you can work in the red KT rating symbol from Penrowe-Calloway, that would be a plus.

Target Market(s)

Old people - so it should be easy to read.

Industry/Entity Type

Business

Contact Information for Business Card

See the specs in the word document below. Also, see the design for my website. The card should have a similar look to the site.

Requirements
Must have
• Everything listed in the business card specs. I don't mind having the address set off at the bottom of the card on its own line.
Should not have
• 1) Any sort of design that could also be used by a tattoo parlour or a tarot card reader, mystic etc.
• 2) There should not be any photographs of me (or anyone else).

```html
<!DOCTYPE html>
<html lang="en">
<head>
<meta charset="utf-8">
<title>Harwell's Law Firm – Business Card</title>
<link href="https://fonts.googleapis.com/css2?family=Tinos:wght@400;700&family=Montserrat:wght@500&display=swap" rel="stylesheet">
<style>
  :root {
    --page-bg: #e9e6e2;
    --card-dark-top: #3a3230;
    --card-dark-mid: #2b2423;
    --card-dark-bottom: #1f1a19;
    --card-light: #e4e4e4;
    --card-light-edge: #c9c9c9;
    --ink-light: #f4f2f0;
    --ink-dark: #3b3b3b;
    --badge-fill: #ffffff;
  }
  * { box-sizing: border-box; margin: 0; padding: 0; }
  html, body { width: 1200px; height: 818px; overflow: hidden; }
  body {
    background: var(--page-bg);
    display: flex;
    align-items: center;
    justify-content: center;
    font-family: "Tinos", "Times New Roman", serif;
  }
  .card {
    position: relative;
    width: 420px;
    height: 735px;
    background: linear-gradient(160deg, var(--card-dark-top) 0%, var(--card-dark-mid) 50%, var(--card-dark-bottom) 100%);
    box-shadow: 0 10px 30px rgba(0,0,0,0.25);
    color: var(--ink-light);
    overflow: hidden;
  }
  .card__header {
    position: absolute;
    top: 62px;
    left: 0; right: 0;
    text-align: center;
  }
  .firm-name { font-size: 38px; font-weight: 400; letter-spacing: 0.5px; }
  .firm-tagline { font-size: 19px; font-style: italic; margin-top: 2px; }
  .lawyer {
    position: absolute;
    top: 190px;
    right: 52px;
    text-align: right;
  }
  .lawyer__name { font-size: 27px; }
  .lawyer__degrees { font-size: 22px; margin-right: 30px; }
  .rating {
    position: absolute;
    top: 300px;
    left: 0; right: 0;
    display: flex;
    flex-direction: column;
    align-items: center;
  }
  .rating__mark {
    width: 78px; height: 78px;
    border-radius: 50%;
    background: var(--badge-fill);
  }
  .rating__name {
    margin-top: 8px;
    font-family: "Montserrat", Arial, sans-serif;
    font-weight: 500;
    font-size: 13px;
  }
  .contact {
    position: absolute;
    top: 415px;
    left: 0; right: 0;
    text-align: center;
    font-size: 20px;
    line-height: 1.3;
  }
  .contact__address { font-size: 18px; margin-top: 4px; }
  .phones {
    position: absolute;
    top: 520px;
    left: 36px; right: 36px;
    display: flex;
    justify-content: space-between;
    font-size: 20px;
  }
  .phones__item { display: flex; align-items: center; gap: 8px; }
  .phones__item svg { width: 20px; height: 20px; fill: var(--ink-light); }
  .card__footer {
    position: absolute;
    left: 0; right: 0; bottom: 0;
    height: 150px;
    background: linear-gradient(180deg, var(--card-light) 0%, var(--card-light-edge) 100%);
    color: var(--ink-dark);
    text-align: center;
    padding-top: 36px;
    font-size: 21px;
    line-height: 1.3;
  }
</style>
</head>
<body>
  <article class="card">
    <header class="card__header">
      <h1 class="firm-name">Harwell's Law Firm</h1>
      <p class="firm-tagline">"Getting the results that matter"</p>
    </header>

    <div class="lawyer">
      <p class="lawyer__name">Daniel R. Harwell</p>
      <p class="lawyer__degrees">B.A. &amp; J.D</p>
    </div>

    <div class="rating">
      <div class="rating__mark" aria-hidden="true"></div>
      <p class="rating__name">Penrowe-Calloway</p>
    </div>

    <div class="contact">
      <p class="contact__web">www.harwellsfirm.ca</p>
      <p class="contact__email">xxxx@harwellsfirm.ca</p>
      <p class="contact__address">12 Larkfield Street West, Ground Floor, Brantford<br>ON N3T 4K2</p>
    </div>

    <div class="phones">
      <p class="phones__item">
        <svg viewBox="0 0 24 24" aria-label="Phone"><path d="M6.6 10.8a15.1 15.1 0 0 0 6.6 6.6l2.2-2.2c.3-.3.7-.4 1-.2 1.1.4 2.3.6 3.6.6.6 0 1 .4 1 1V20c0 .6-.4 1-1 1A17 17 0 0 1 3 4c0-.6.4-1 1-1h3.5c.6 0 1 .4 1 1 0 1.3.2 2.5.6 3.6.1.3 0 .7-.2 1z"/></svg>
        555-210-xxxx
      </p>
      <p class="phones__item">
        <svg viewBox="0 0 24 24" aria-label="Fax"><path d="M7 3h10v5H7zM4 9h16a2 2 0 0 1 2 2v6h-4v4H6v-4H2v-6a2 2 0 0 1 2-2zm4 7v3h8v-3z"/></svg>
        555.318.xxxx
      </p>
    </div>

    <footer class="card__footer">
      <p>Barrister, Solicitor &amp; Notary Public, Lawyer</p>
      <p>Litigation Counsel, Trial Lawyer</p>
    </footer>
  </article>
</body>
</html>
```